Roofing web site brel roofing

Look at some of our competitors web page we like something similar with NYC roofing
https://www.dovantileworks.example/
Maybe a skyline picture of nyc at the home page with a picture of flat roofing installation

Target Market(s)

Commercial and residential flat roofs

Industry/Entity Type

Flat Roofing industry

Coding

Coded - Design and coding required

Number of Pages Required

2 page

Font styles to use
Decorative
Script

Colors

Designer to choose colors to be used in the design.

Requirements
Must have
• At BREL Roofing, we are a trusted and reputable roofing company specializing in new construction flat roof installation and repair. With years of experience in the industry, we take pride in providing exceptional roofing solutions to our valued clients. Our team of highly skilled and dedicated roofing professionals understands the unique challenges and requirements of new construction projects. We work closely with builders, contractors, and architects to design and install flat roofs that meet the specific needs of each project. From commercial buildings to residential complexes, we have the expertise to deliver reliable and durable roofing solutions. When it comes to flat roof repairs, we are your go-to experts. Our experienced technicians conduct thorough inspections to identify the root cause of any issues your roof may be experiencing. We utilize the latest industry techniques and high-quality materials to efficiently repair your flat roof, ensuring its integrity and longevity. At BREL Roofing, we prioritize customer satisfaction above all else. We believe in building strong relationships with our clients by providing exceptional craftsmanship and outstanding customer service. Our team is dedicated to delivering projects on time, within budget, and to the highest standards of quality. We understand that a well-maintained roof is essential for protecting your property and ensuring the safety of its occupants. That's why we use only the best materials and employ skilled professionals who are trained in the latest roofing practices. Our commitment to excellence is evident in every project we undertake. As a fully licensed and insured roofing company, we prioritize safety and adhere to industry regulations and best practices. We take every precaution to create a safe working environment for our team and minimize any disruptions to your daily routine. When you choose BREL Roofing, you can trust that you are working with a reliable and reputable company that will deliver exceptional results. We are committed to exceeding your expectations and providing you with a roof that is built to last. Contact us today for all your new construction flat roof installation and repair needs.
Nice to have
• NYC skyline background with commercial roofing pictures of torching roofing

```html
<!DOCTYPE html>
<html lang="en">
<head>
<meta charset="utf-8">
<title>BREL Roofing — Flat Roof Installation &amp; Repair</title>
<link href="https://fonts.googleapis.com/css2?family=Russo+One&family=Poppins:wght@400;500;600;700&display=swap" rel="stylesheet">
<style>
:root{
  --orange:#f26a1f;
  --orange-dark:#c84f12;
  --orange-deep:#a9400c;
  --ink:#1c1c1c;
  --text:#555;
  --black:#050505;
  --white:#fff;
  --line:#e6e6e6;
  --navy:#1f3346;
}
*{box-sizing:border-box;margin:0;padding:0}
html,body{width:1200px;height:4673px;overflow:hidden}
body{position:relative;font-family:"Poppins",sans-serif;color:var(--text);background:var(--white)}
.abs{position:absolute}
.display{font-family:"Russo One",sans-serif;color:var(--ink);letter-spacing:.5px}
.btn{position:absolute;display:flex;align-items:center;justify-content:center;background:var(--orange);color:var(--white);font-family:"Russo One",sans-serif;font-size:16px;border-radius:3px;letter-spacing:.3px}
.eyebrow{font-family:"Russo One",sans-serif;color:var(--orange);letter-spacing:4px;font-size:15px}
.rule{position:absolute;height:4px;width:54px;background:var(--orange)}

/* top bar & header */
.topbar{left:0;top:0;width:1200px;height:47px;background:var(--black);color:var(--white);font-size:15px;display:flex;align-items:center;justify-content:center}
.header{left:0;top:47px;width:1200px;height:89px;background:var(--white)}
.brand{position:absolute;display:flex;align-items:center;gap:10px;font-family:"Poppins",sans-serif;font-weight:600;white-space:nowrap}
.brand .mark{display:block;width:14px;height:14px}
.header .brand{left:112px;top:28px;font-size:24px;color:var(--ink)}
.header .brand .mark{background:var(--orange)}
.call{left:530px;top:6px;display:flex;align-items:center;gap:10px;font-size:18px;color:var(--ink)}
.call b{font-family:"Russo One",sans-serif;font-weight:400;font-size:17px}
.call span{font-family:"Russo One",sans-serif;color:var(--orange);font-size:24px;margin-left:8px}
.nav{left:336px;top:44px;width:570px;border-top:1px solid var(--line);padding-top:12px;display:flex;gap:44px;font-size:13px;color:var(--ink)}
.nav .active{color:var(--orange);font-weight:600;margin-left:30px}
.estimate{left:912px;top:0;width:288px;height:89px;background:var(--orange);color:var(--white);font-family:"Russo One",sans-serif;font-size:23px;display:flex;align-items:center;justify-content:center}

/* hero */
.hero{left:0;top:136px;width:1200px;height:589px;overflow:hidden;background:linear-gradient(180deg,#3d5a73 0%,#1f3346 55%,#0e1a26 100%)}
.hero-photo{position:absolute;inset:0;background:linear-gradient(160deg,#8db2d0 0%,#b7c7d2 40%,#4e5a63 75%,#2a2e31 100%);clip-path:polygon(798px 0,1200px 0,1200px 589px,462px 589px)}
.hero-edge{position:absolute;inset:0;pointer-events:none}
.hero .welcome{left:112px;top:132px;color:#e6e6e6;font-size:15px}
.hero h1{position:absolute;left:112px;top:156px;font-family:"Russo One",sans-serif;font-weight:400;color:var(--white);font-size:30px;line-height:34px}
.hero h2{position:absolute;left:112px;font-family:"Russo One",sans-serif;font-weight:400;color:var(--white);font-size:30px;line-height:34px}
.slider{left:112px;top:530px;display:flex;align-items:center;gap:6px;color:#ddd;font-size:17px}
.slider i{display:block;width:34px;height:2px;background:#aaa}
.slider i.on{background:var(--orange);height:4px}

/* about */
.about-photo{left:110px;top:832px;width:733px;height:589px;background:linear-gradient(135deg,#6a7c8c 0%,#2f3236 45%,#6b4a2e 80%,#3a2a1c 100%);clip-path:polygon(0 0,690px 0,733px 70px,733px 520px,690px 589px,0 589px)}
.about-card{left:598px;top:912px;width:490px;height:430px;background:var(--white);box-shadow:0 6px 26px rgba(0,0,0,.14)}
.about-card .eyebrow{position:absolute;left:50px;top:33px}
.about-card h3{position:absolute;left:46px;top:65px;font-size:38px;line-height:40px;font-weight:400}
.about-card p{position:absolute;left:48px;top:190px;width:410px;font-size:14.5px;line-height:25px;text-align:justify}

/* team */
.team{width:491px;height:432px;background:var(--white);box-shadow:0 4px 22px rgba(0,0,0,.13);top:1519px}
.team h4{position:absolute;left:44px;top:50px;font-size:27px;font-weight:400}
.team .role{position:absolute;left:44px;top:92px;color:var(--orange);font-family:"Russo One",sans-serif;font-size:15.5px;line-height:24px;letter-spacing:.5px}
.team .rule{left:44px;top:156px}
.avatar{position:absolute;right:46px;top:30px;width:140px;height:140px;border-radius:50%;border:3px solid var(--orange);background:linear-gradient(160deg,#c9d2da,#8a96a1)}
.team p{position:absolute;left:44px;top:195px;width:410px;font-size:15px;line-height:25px;text-align:justify}
.team .btn{left:44px;top:341px;width:155px;height:47px}

/* features */
.feat-photo{left:290px;top:2043px;width:910px;height:590px;background:linear-gradient(120deg,#2a2c2f 0%,#3a3d41 35%,#5a4128 70%,#7d5a38 100%)}
.feat-col{left:74px;top:2043px;width:216px;height:590px;background:var(--orange)}
.feat-item{position:absolute;left:0;width:216px;height:200px;padding:22px 36px 0 36px;color:var(--white)}
.feat-item.mid{background:var(--orange-deep)}
.feat-item h5{font-family:"Russo One",sans-serif;font-weight:400;font-size:15px;line-height:18px;margin-top:10px}
.feat-item p{font-size:9.5px;line-height:15px;margin-top:6px}
.feat-text{left:310px;top:2215px;width:365px;color:var(--white)}
.feat-text h3{font-family:"Russo One",sans-serif;font-weight:400;font-size:23px;line-height:28px}
.feat-text p{font-size:14px;line-height:22px;margin-top:12px}
.feat-text .btn{position:relative;width:153px;height:44px;margin-top:16px}

/* faq */
.faq-label{left:0;width:1200px;top:2722px;text-align:center}
.faq-title{left:0;width:1200px;top:2752px;text-align:center;font-size:40px}
.faq-item{left:227px;width:747px;background:var(--white);border-radius:22px;box-shadow:0 3px 14px rgba(0,0,0,.12);display:flex;align-items:center;padding:0 28px;font-size:14.5px;font-weight:500;color:var(--ink)}
.faq-item .q{display:flex;align-items:center;gap:9px;flex:1}
.faq-item .sign{font-size:20px}
.faq-open{left:227px;top:2984px;width:747px;height:140px;background:var(--white);border-radius:22px;box-shadow:0 3px 14px rgba(0,0,0,.12);overflow:hidden}
.faq-open .head{height:48px;background:var(--orange);color:var(--white);display:flex;align-items:center;padding:0 28px;font-size:14.5px;font-weight:500}
.faq-open .head .q{display:flex;align-items:center;gap:9px;flex:1}
.faq-open p{padding:16px 50px 0 50px;font-size:14.5px;line-height:24px}

/* gallery */
.gallery{left:0;top:3222px;width:1200px;height:917px;background:var(--orange)}
.gallery .eyebrow{position:absolute;left:0;width:1200px;top:56px;text-align:center;color:var(--white)}
.gallery h3{position:absolute;left:0;width:1200px;top:96px;text-align:center;color:var(--white);font-size:40px;font-weight:400}
.gallery .rule{left:573px;top:157px;background:var(--white)}
.grid{position:absolute;left:69px;top:183px;display:grid;grid-template-columns:repeat(5,206px);grid-auto-rows:206px;gap:11px}
.gallery .btn{left:523px;top:636px;width:154px;height:46px;background:var(--white);color:var(--orange)}

/* footer */
.footer{left:0;top:4139px;width:1200px;height:534px;background:var(--black)}
.news{left:179px;top:3992px;width:842px;height:308px;background:var(--white);border:9px solid var(--orange);outline:5px solid #111;border-radius:6px}
.news h3{position:absolute;left:0;width:824px;top:36px;text-align:center;font-size:27px;line-height:37px;font-weight:400;color:var(--ink)}
.news .lead{position:absolute;left:0;width:824px;top:126px;text-align:center;font-size:14px;color:var(--ink);font-weight:500}
.field{position:absolute;top:152px;width:274px;height:37px;background:#111;color:#ddd;font-size:12px;display:flex;align-items:center;padding-left:18px;border-radius:2px}
.news .btn{left:344px;top:218px;width:154px;height:46px}
.footer .brand{left:161px;top:302px;font-size:28px;color:var(--white)}
.footer .brand .mark{background:var(--white)}
.fcol{position:absolute;top:262px;color:var(--white)}
.fcol h6{font-family:"Russo One",sans-serif;font-weight:400;font-size:15px;letter-spacing:.5px}
.fcol .rule{position:relative;display:block;width:34px;height:3px;margin:10px 0 18px}
.fcol li{list-style:none;font-size:12px;line-height:22px}
.contact-row{display:flex;align-items:center;gap:16px;font-size:13px;line-height:17px;margin-bottom:20px}
.contact-row .dot{width:34px;height:34px;border-radius:50%;background:#2b2b2b;display:flex;align-items:center;justify-content:center}
.footer .bottom{position:absolute;left:110px;top:457px;width:980px;border-top:1px solid #555}
.footer .copy{position:absolute;left:0;width:1200px;top:485px;text-align:center;color:var(--white);font-size:12px}
</style>
</head>
<body>

<div class="abs topbar">GET A FREE QUOTE! FREE INSPECTION FOR DAMAGE TO SUBMIT TO YOUR INSURANCE COMPANY!</div>

<header class="abs header">
  <div class="brand"><span class="mark"></span><span>BREL Roofing</span></div>
  <div class="abs call">
    <svg width="22" height="22" viewBox="0 0 24 24"><path fill="#f26a1f" d="M6.6 10.8a15.1 15.1 0 006.6 6.6l2.2-2.2a1 1 0 011-.25 11.4 11.4 0 003.6.57 1 1 0 011 1V20a1 1 0 01-1 1A17 17 0 013 4a1 1 0 011-1h3.5a1 1 0 011 1c0 1.25.2 2.45.57 3.57a1 1 0 01-.25 1z"/></svg>
    <b>Call Us Today!</b><span>(555) 014-2290</span>
  </div>
  <nav class="abs nav">
    <span class="active">HOME</span><span>CONTACT US</span><span>PHOTO GALLERY</span><span>SERVICES</span><span>ABOUT US</span>
  </nav>
  <div class="abs estimate">GET A FREE ESTIMATE</div>
</header>

<section class="abs hero">
  <div class="abs" role="img" aria-label="New York City skyline at dusk across the river" style="inset:0;background:linear-gradient(180deg,rgba(120,150,175,.35),rgba(15,28,40,.2))"></div>
  <div class="hero-photo" role="img" aria-label="Roofer torching a flat roof membrane on a city rooftop"></div>
  <svg class="hero-edge" width="1200" height="589"><line x1="798" y1="0" x2="462" y2="589" stroke="#fff" stroke-width="6"/></svg>
  <div class="abs welcome">WELCOME</div>
  <h1>Professional &amp; Affordable<br>Roofing Services.</h1>
  <h2 style="top:242px">Call Today For a Free Quote!</h2>
  <h2 style="top:296px">Storm damage, roof installation,<br>roof repair</h2>
  <div class="btn" style="left:112px;top:399px;width:154px;height:46px;border:2px solid #fff">BOOK NOW</div>
  <div class="abs slider"><span style="color:var(--orange)">01</span><i class="on"></i><i></i><i></i><i></i><i></i><span>05</span></div>
</section>

<section>
  <div class="abs about-photo" role="img" aria-label="Two roofers inspecting plans on a dark metal roof"></div>
  <div class="abs about-card">
    <div class="eyebrow">ABOUT</div>
    <h3 class="display">BREL CONSTRUCTION<br>OF NY</h3>
    <p>At BREL Roofing, we are a trusted and reputable roofing company specializing in new construction flat roof installation and repair. With years of experience in the industry, we take pride in providing exceptional roofing solutions to our valued clients. Our team of highly skilled</p>
    <div class="btn" style="left:50px;top:345px;width:154px;height:46px">FIND OUT MORE</div>
  </div>
</section>

<section>
  <div class="abs team" style="left:80px">
    <h4 class="display">DANA R</h4>
    <div class="role">BUSINESS MANAGER &amp;<br>DEVELOPMENT</div>
    <div class="rule"></div>
    <div class="avatar" role="img" aria-label="Portrait of Dana R in an orange hard hat"></div>
    <p>Victor's daughter Dana has been around the business since she was a kid. With a degree in Green Construction, she incorporates the latest in green options into your project. Saving the planet, while saving you money, is her goal!</p>
    <div class="btn">FIND OUT MORE</div>
  </div>
  <div class="abs team" style="left:629px">
    <h4 class="display">OWEN P</h4>
    <div class="role">PROJECT LEADER</div>
    <div class="rule" style="top:128px"></div>
    <div class="avatar" role="img" aria-label="Portrait of Owen P in a white hard hat"></div>
    <p>Owen is Victor's right hand man. He's all about structure and organization. Through general oversight, his focus is to bring your job to completion on time and within budget.</p>
    <div class="btn">FIND OUT MORE</div>
  </div>
</section>

<section>
  <div class="abs feat-photo" role="img" aria-label="Roofers installing dark metal roofing panels on a timber house"></div>
  <div class="abs" style="left:290px;top:2043px;width:420px;height:590px;background:linear-gradient(90deg,rgba(20,20,20,.85),rgba(20,20,20,0))"></div>
  <div class="abs feat-col" style="box-shadow:0 6px 20px rgba(0,0,0,.2)">
    <div class="feat-item" style="top:0">
      <svg width="50" height="30" viewBox="0 0 50 30" fill="none" stroke="#fff" stroke-width="2"><path d="M4 28L12 4h26l8 24z"/><path d="M8 16h34M18 4l-4 24M32 4l4 24M25 4v24"/></svg>
      <h5>RELIABLE ROOFING PROFESSIONALS</h5>
      <p>As specialists in residential and commercial roofing services, we are dedicated customer...</p>
    </div>
    <div class="feat-item mid" style="top:200px">
      <svg width="44" height="38" viewBox="0 0 44 38" fill="none" stroke="#fff" stroke-width="2"><path d="M4 18L22 4l18 14M8 15v20h28V15"/><rect x="15" y="20" width="14" height="15"/><path d="M30 6v6"/></svg>
      <h5>INDIVIDUALIZED ROOFING OPTIONS</h5>
      <p>We provide a full consultation to explain your available options so that you can...</p>
    </div>
    <div class="feat-item" style="top:400px">
      <svg width="44" height="44" viewBox="0 0 44 44" fill="none" stroke="#fff" stroke-width="2"><circle cx="22" cy="18" r="12"/><circle cx="22" cy="18" r="7"/><path d="M15 28l-5 12 6-3 3 5 3-9M29 28l5 12-6-3-3 5-3-9"/></svg>
      <h5>SATISFACTION GUARANTEED</h5>
      <p>We strive to save you both time and money by combining roofing knowledge, the highest quality...</p>
    </div>
  </div>
  <div class="abs feat-text">
    <h3>INDIVIDUALIZED ROOFING<br>OPTIONS</h3>
    <p>We provide a full consultation to explain your available options so that you can choose the roofing plan that's right for your home or business. We will work with you and adhere to your personal needs, and then we'll be in contact through the whole project.</p>
    <div class="btn">FIND OUT MORE</div>
  </div>
</section>

<section>
  <div class="abs eyebrow faq-label">FAQ</div>
  <div class="abs display faq-title">FREQUENTLY ASKED QUESTIONS</div>
  <div class="rule" style="left:573px;top:2814px"></div>
  <div class="abs faq-item" style="top:2846px;height:46px">
    <span class="q"><svg width="16" height="16" viewBox="0 0 16 16" fill="none" stroke="#333" stroke-width="1.3"><circle cx="8" cy="8" r="7"/><path d="M6 6.2a2 2 0 113 1.7c-.7.4-1 .8-1 1.6M8 11.6v.4"/></svg>Do you provide homeowners insurance inspections?</span><span class="sign">+</span>
  </div>
  <div class="abs faq-item" style="top:2913px;height:48px">
    <span class="q"><svg width="16" height="16" viewBox="0 0 16 16" fill="none" stroke="#333" stroke-width="1.3"><circle cx="8" cy="8" r="7"/><path d="M6 6.2a2 2 0 113 1.7c-.7.4-1 .8-1 1.6M8 11.6v.4"/></svg>Do I have to replace gutters and downspouts?</span><span class="sign">+</span>
  </div>
  <div class="abs faq-open">
    <div class="head"><span class="q"><svg width="16" height="16" viewBox="0 0 16 16" fill="none" stroke="#fff" stroke-width="1.3"><circle cx="8" cy="8" r="7"/><path d="M6 6.2a2 2 0 113 1.7c-.7.4-1 .8-1 1.6M8 11.6v.4"/></svg>What if my newly installed roof leaks?</span><span>-</span></div>
    <p>We stand by our work, so if there are any leaks in the new roof, we cover the repair cost to the roof and any damage caused by the leak.</p>
  </div>
</section>

<section class="abs gallery">
  <div class="eyebrow">GALLERY</div>
  <h3 class="display">PHOTO GALLERY</h3>
  <div class="rule"></div>
  <div class="grid">
    <div role="img" aria-label="Roofer nailing wooden roof boards" style="background:linear-gradient(135deg,#8fa6b8,#c9a27a)"></div>
    <div role="img" aria-label="Grey standing seam metal roof under cloudy sky" style="background:linear-gradient(160deg,#4a5560,#9aa3a8)"></div>
    <div role="img" aria-label="Hand repairing stone masonry with a trowel" style="background:linear-gradient(135deg,#a89a88,#e0d8cc)"></div>
    <div role="img" aria-label="Hand painting a wall with a brush" style="background:linear-gradient(135deg,#c8b48a,#e8e2d6)"></div>
    <div role="img" aria-label="Dark asphalt shingle roof against the sky" style="background:linear-gradient(180deg,#b8c8d6,#3e4348)"></div>
    <div role="img" aria-label="Roll of roofing membrane being torched" style="background:linear-gradient(180deg,#dfe6ec,#3a3c40)"></div>
    <div role="img" aria-label="Roofers working on a grey flat roof" style="background:linear-gradient(135deg,#6c7075,#42464a)"></div>
    <div role="img" aria-label="Worker on a yellow ladder" style="background:linear-gradient(135deg,#e6e6e2,#c7b14a)"></div>
    <div role="img" aria-label="Gas torch and membrane roll on a roof" style="background:linear-gradient(180deg,#8c9096,#2e3034)"></div>
    <div role="img" aria-label="Flame torching bitumen roof seams" style="background:linear-gradient(135deg,#5a7a9c,#2c3a4a 70%,#d0782a)"></div>
  </div>
  <div class="btn">FIND OUT MORE</div>
</section>

<footer class="abs footer">
  <div class="brand"><span class="mark"></span><span>BREL Roofing</span></div>
  <div class="fcol" style="left:442px">
    <h6>QUICK LINKS</h6><span class="rule"></span>
    <ul><li>HOME</li><li>CONTACT US</li><li>PHOTO GALLERY</li><li>SERVICES</li><li>ABOUT US</li></ul>
  </div>
  <div class="fcol" style="left:631px">
    <h6>LINKS</h6><span class="rule"></span>
    <ul><li>COPYRIGHT</li><li>TERMS OF USE</li><li>PRIVACY POLICY</li><li>ACCESSIBILITY</li><li>SITEMAP</li></ul>
  </div>
  <div class="fcol" style="left:812px">
    <h6>CONTACT US</h6><span class="rule"></span>
    <div class="contact-row"><span class="dot"><svg width="16" height="16" viewBox="0 0 24 24"><path fill="#f26a1f" d="M6.6 10.8a15.1 15.1 0 006.6 6.6l2.2-2.2a1 1 0 011-.25 11.4 11.4 0 003.6.57 1 1 0 011 1V20a1 1 0 01-1 1A17 17 0 013 4a1 1 0 011-1h3.5a1 1 0 011 1c0 1.25.2 2.45.57 3.57a1 1 0 01-.25 1z"/></svg></span><span>Call Us<br>555-014-2290</span></div>
    <div class="contact-row"><span class="dot"><svg width="16" height="14" viewBox="0 0 16 12" fill="none" stroke="#f26a1f" stroke-width="1.5"><rect x="1" y="1" width="14" height="10"/><path d="M1 1l7 6 7-6"/></svg></span><span>Email<br>HELLO@BRELROOFING.EXAMPLE</span></div>
  </div>
  <div class="bottom"></div>
  <div class="copy">COPYRIGHT © 2024 BREL CONSTRUCTION OF NY ROOFING - ALL RIGHTS RESERVED.</div>
</footer>

<div class="abs news">
  <h3 class="display">FLAT ROOF INSTALLATION ROOF REPAIR STORM<br>DAMAGE INSURANCE SPECIALISTS</h3>
  <div class="lead">Sign up to receive maintenance reminders and hear about our latest projects.</div>
  <div class="field" style="left:131px">Your Name</div>
  <div class="field" style="left:418px">Email</div>
  <div class="btn">SIGN UP</div>
</div>

</body>
</html>
```